Business Card and Stationery for Interior Design Company
Silver Kettle Design
Designers,
On the back of my card on want the following services listed:
Interior Decorating
Room Redesign
Space Planning
Paint Color Selection
Furnishings & Accessories
The fonts used in the logo are as follows:
fonts:
Kozuka Mincho Pr6N M
Miss Le Gatees (modified)
RT/KPF/JN Team
My tagline "Design with Vision" does NOT have to be the same font as the original logo font. Neither does my Name. In fact, tagline should probably be italic and my Name I'd like to see perhaps in a similar script font like the word INTERIOR.

```html
<!DOCTYPE html>
<html lang="en">
<head>
<meta charset="utf-8">
<title>Silver Kettle Design – Business Card Back</title>
<link rel="stylesheet" href="https://fonts.googleapis.com/css2?family=Cormorant+Garamond:wght@500;600&family=Great+Vibes&display=swap">
<style>
  :root {
    --page: #1c1c1e;
    --card-white: #fbfbfb;
    --stripe-grey: #ececec;
    --ink: #5a5a5a;
    --teal: #8fcfcb;
    --teal-deep: #6fb9b5;
    --gold: #c9a84e;
    --tagline-ink: #3d3d3d;
  }
  * { box-sizing: border-box; margin: 0; padding: 0; }
  html, body {
    width: 1200px;
    height: 901px;
    overflow: hidden;
    background: var(--page);
  }
  .stage {
    width: 1200px;
    height: 901px;
    display: flex;
    align-items: center;
    justify-content: center;
  }
  .card {
    position: relative;
    width: 470px;
    height: 820px;
    background:
      repeating-linear-gradient(90deg,
        var(--card-white) 0 47px,
        var(--stripe-grey) 47px 94px);
    display: flex;
    flex-direction: column;
    align-items: center;
    overflow: hidden;
  }
  .logo {
    margin-top: 62px;
    display: flex;
    flex-direction: column;
    align-items: center;
  }
  .logo-illustration {
    width: 150px;
    height: 92px;
    border-radius: 4px;
    background: linear-gradient(160deg, #e4ecea 0%, #a9d8d4 55%, #e9e2cf 100%);
  }
  .logo-name {
    margin-top: 14px;
    font-family: "Cormorant Garamond", serif;
    font-weight: 500;
    font-size: 36px;
    line-height: 1.05;
    color: var(--ink);
    text-align: center;
  }
  .services-frame {
    margin-top: 40px;
    position: relative;
    width: 310px;
    height: 230px;
    display: flex;
    align-items: center;
    justify-content: center;
  }
  .services-frame svg {
    position: absolute;
    inset: 0;
  }
  .services {
    position: relative;
    list-style: none;
    text-align: center;
    font-family: "Cormorant Garamond", serif;
    font-weight: 500;
    font-size: 22px;
    line-height: 1.4;
    color: var(--ink);
  }
  .tagline-band {
    position: absolute;
    left: 0;
    right: 0;
    bottom: 0;
    height: 165px;
    background: linear-gradient(180deg, var(--teal) 0%, var(--teal-deep) 100%);
    display: flex;
    align-items: center;
    justify-content: center;
  }
  .tagline {
    font-family: "Great Vibes", cursive;
    font-size: 50px;
    color: var(--tagline-ink);
  }
</style>
</head>
<body>
<main class="stage">
  <article class="card">
    <header class="logo">
      <div class="logo-illustration" role="img" aria-label="Illustration of an armchair and lamp for the Silver Kettle Design logo"></div>
      <div class="logo-name">Silver Kettle<br>Design</div>
    </header>

    <section class="services-frame">
      <svg width="310" height="230" viewBox="0 0 310 230" aria-hidden="true">
        <rect x="6" y="6" width="298" height="218" rx="18" fill="none" stroke="var(--gold)" stroke-width="2.5"/>
        <rect x="13" y="13" width="284" height="204" rx="13" fill="none" stroke="var(--gold)" stroke-width="1"/>
      </svg>
      <ul class="services">
        <li>Interior Decorating</li>
        <li>Room Redesign</li>
        <li>Space Planning</li>
        <li>Paint Color Selection</li>
        <li>Furnishings &amp; Accessories</li>
      </ul>
    </section>

    <footer class="tagline-band">
      <p class="tagline">Design with Vision</p>
    </footer>
  </article>
</main>
</body>
</html>
```